Building Design company needing a letterhead

We need a letter head for our Building Design company to send letters etc. to our clients, consultants, councils etc. We would like to see our logo used and company colours. I have attached our style guide and an example of our current letterheads. Top left we would like our logo, top right we would like the company details and at the footer we would like some sort of image/design etc. that suits our brand. I like the Torvik Design letterhead attached.

Target Market(s)

Professionals, Councils, Consultants, Mums & Dads

Industry/Entity Type

Architecture

Font styles to use
Other font styles liked:
• refer the design style guide

Colors
f37122
000000
1b1b1b

Requirements
Must have
• Must have the minimum of a logo, company details and footer
Nice to have
• An image/design made for the footer that would suite our brand and website at www.quarvedesign.com.au. Also it would be nice to include the GMKLE logo somewhere perhaps included in the footer.
Should not have
• Large images in the header. I just want the logo and company details.

```html
<!DOCTYPE html>
<html lang="en">
<head>
<meta charset="utf-8">
<title>Quarve Design Letterhead</title>
<link href="https://fonts.googleapis.com/css2?family=Montserrat:wght@600;700&family=Questrial&display=swap" rel="stylesheet">
<style>
  :root {
    --brand-orange: #f37122;
    --brand-black: #000000;
    --brand-charcoal: #1b1b1b;
    --text-grey: #555555;
    --stage: #3b3430;
    --paper: #ffffff;
    --peach: #f6d9c8;
    --logo-border: #c9c9c9;
  }
  * { box-sizing: border-box; margin: 0; padding: 0; }
  html, body { width: 1200px; height: 1200px; overflow: hidden; }
  body { background: var(--stage); font-family: "Questrial", sans-serif; }

  .letterhead {
    position: absolute; left: 200px; top: 35px;
    width: 800px; height: 1130px;
    background: var(--paper);
    overflow: hidden;
  }

  .header-image {
    position: absolute; left: 0; top: 0; width: 100%; height: 230px;
    background: linear-gradient(100deg, #c8480f 0%, var(--brand-orange) 28%, #f7a06a 48%, var(--peach) 70%, #fbeee6 100%);
  }
  .header-sweep, .footer-sweep { position: absolute; left: 0; width: 100%; }
  .header-sweep { top: 90px; height: 220px; }
  .footer-sweep { bottom: 170px; height: 200px; }

  .logo-box {
    position: absolute; left: 90px; top: 70px;
    width: 270px; height: 110px;
    background: var(--paper);
    border: 6px solid var(--logo-border);
    display: flex; align-items: center; justify-content: center; gap: 14px;
  }
  .logo-square { width: 30px; height: 30px; background: var(--brand-orange); }
  .logo-name {
    font-family: "Montserrat", sans-serif; font-weight: 700;
    font-size: 26px; line-height: 1.05; letter-spacing: 2px;
    color: var(--brand-charcoal);
  }

  .company-details {
    position: absolute; right: 60px; top: 200px;
    font-family: "Montserrat", sans-serif; font-weight: 600;
    font-size: 11px; line-height: 1.45; color: var(--brand-charcoal);
  }
  .company-details .gap { margin-top: 8px; }
  .company-details .web {
    margin-top: 6px; font-size: 14px; font-weight: 700; color: var(--brand-orange);
  }

  .letter-title {
    position: absolute; left: 90px; top: 350px;
    font-family: "Montserrat", sans-serif; font-weight: 700;
    font-size: 17px; color: var(--brand-black);
  }
  .letter-body {
    position: absolute; left: 90px; top: 395px; width: 620px;
    font-size: 13.5px; line-height: 1.62; color: var(--text-grey);
  }

  .signature {
    position: absolute; left: 420px; top: 700px; width: 290px;
    border-top: 1.5px solid var(--brand-charcoal);
    padding-top: 10px; text-align: center;
    font-family: "Montserrat", sans-serif; font-weight: 700;
    font-size: 16px; color: var(--brand-black);
  }

  .footer-image {
    position: absolute; left: 0; bottom: 0; width: 100%; height: 300px;
    background: linear-gradient(180deg, rgba(255,255,255,0) 0%, #f3d2bf 35%, #d98a5c 75%, #b45a2a 100%);
  }
</style>
</head>
<body>
  <main class="letterhead">
    <div class="header-image" role="img" aria-label="Warm orange architectural render of angled building forms"></div>
    <svg class="header-sweep" viewBox="0 0 800 220" preserveAspectRatio="none" aria-hidden="true">
      <path d="M0 200 C220 60 520 40 800 90 L800 220 L0 220 Z" fill="#ffffff"/>
      <path d="M0 200 C220 60 520 40 800 90" fill="none" stroke="#f2c9b1" stroke-width="3"/>
      <path d="M0 215 C260 100 540 80 800 120" fill="none" stroke="#f7e2d6" stroke-width="2"/>
    </svg>

    <div class="logo-box">
      <span class="logo-square"></span>
      <span class="logo-name">QUARVE<br>DESIGN</span>
    </div>

    <address class="company-details" style="font-style:normal">
      <div>Unit 4/22 Harlow Way Dunmore WA 6412</div>
      <div>PO Box 3187 Dunmore North WA 6412</div>
      <div class="gap">PH (08) 6190 4418</div>
      <div>ABN 41 302 758 116</div>
      <div class="gap">admin@quarvedesign.com.au</div>
      <div class="web">www.quarvedesign.com.au</div>
    </address>

    <h1 class="letter-title">Lorem ipsum dolor</h1>
    <p class="letter-body">Lorem ipsum dolor sit amet, consectetuer adipiscing elit. Aenean commodo ligula eget dolor. Aenean massa. Cum sociis natoque penatibus et magnis dis parturient montes, nascetur ridiculus mus. Donec quam felis, ultricies nec, pellentesque eu, pretium quis, sem. Nulla consequat massa quis enim. Donec pede justo, fringilla vel, aliquet nec, vulputate eget, arcu. In enim justo, rhoncus ut, imperdiet a, venenatis vitae, justo. Nullam dictum felis eu pede mollis pretium. Integer tincidunt. Cras dapibus. Vivamus elementum semper nisi. Aenean vulputate eleifend tellus. Aenean leo ligula, porttitor eu, consequat vitae, eleifend ac, enim. Aliquam lorem ante, dapibus in, viverra quis, feugiat a, tellus. Phasellus viverra nulla ut metus varius laoreet. Quisque rutrum. Aenean imperdiet. Etiam ultricies nisi vel augue. Curabitur ullamcorper ultricies nisi. Nam eget dui. Etiam rhoncus. Maecenas tempus, tellus eget condimentum rhoncus, sem quam semper libero, sit amet adipiscing sem neque sed ipsum. Nam quam nunc, blandit vel, luctus pulvinar, hendrerit id, lorem. Maecenas nec odio et ante tincidunt tempus. Donec vitae sapien ut libero venenatis faucibus. Nullam quis ante. Etiam sit amet orci eget eros faucibus tincidunt. Duis leo. Sed fringilla mauris sit amet nibh. Donec sodales sagittis magna. Sed consequat, leo eget bibendum sodales, augue velit cursus nunc.</p>

    <div class="signature">Lorem ipsum dolor</div>

    <div class="footer-image" role="img" aria-label="Soft orange architectural render of building edges fading into the page"></div>
    <svg class="footer-sweep" viewBox="0 0 800 200" preserveAspectRatio="none" aria-hidden="true">
      <path d="M0 40 C200 170 560 190 800 150" fill="none" stroke="#f0c4aa" stroke-width="3"/>
      <path d="M0 70 C240 190 580 200 800 180" fill="none" stroke="#f6ddcd" stroke-width="2"/>
    </svg>
  </main>
</body>
</html>
```